resleeving

we need a revamped flyer to email to our existing customers

ensure all spelling is correct

if using sentences make sure to use centre margins

```html
<!DOCTYPE html>
<html lang="en">
<head>
<meta charset="utf-8">
<title>Stainless Steel Resleeving – Summit Brake Works</title>
<link href="https://fonts.googleapis.com/css2?family=Barlow:wght@400;500;600;700&family=Barlow+Condensed:wght@600;700&display=swap" rel="stylesheet">
<style>
  :root {
    --yellow: #ffd400;
    --charcoal: #2d2d2d;
    --footer: #3a3a3a;
    --ink: #111111;
    --white: #ffffff;
    --label: #e2e2e2;
    --photo-steel: #8a8a8a;
    --photo-dark: #4a4a4a;
  }
  * { margin: 0; padding: 0; box-sizing: border-box; }
  html, body { width: 848px; height: 1200px; overflow: hidden; background: var(--charcoal); }
  .flyer {
    position: relative; width: 848px; height: 1200px; overflow: hidden;
    background: var(--charcoal);
    font-family: "Barlow", Arial, sans-serif; color: var(--white);
  }
  .swoosh { position: absolute; inset: 0; }
  .coil-photo {
    position: absolute; left: 420px; top: 0; width: 428px; height: 140px;
    background: linear-gradient(120deg, #5a5a5a, #2b2b2b);
  }
  .brand {
    position: absolute; left: 46px; top: 204px;
    display: flex; align-items: center; gap: 10px;
    font-weight: 700; font-size: 21px; letter-spacing: 0.5px;
    color: var(--ink); text-transform: uppercase;
  }
  .brand-square { width: 20px; height: 20px; background: var(--ink); }
  .tagline {
    position: absolute; left: 264px; top: 88px; z-index: 2;
    font-weight: 500; font-size: 25px; line-height: 27px; color: var(--ink);
  }
  .caliper-photo {
    position: absolute; left: 384px; top: 146px; width: 380px; height: 150px;
    border-radius: 40px;
    background: radial-gradient(ellipse at 45% 55%, #9a9a9a, #6e6e6e 55%, rgba(110,110,110,0) 78%);
  }
  .lever-photo {
    position: absolute; left: 636px; top: 54px; width: 128px; height: 110px;
    border-radius: 30px;
    background: radial-gradient(ellipse at 50% 50%, #b39a5a, rgba(150,130,70,0) 75%);
  }
  .headline { position: absolute; left: 0; top: 312px; width: 848px; text-align: center; }
  .headline-top {
    font-weight: 700; font-size: 42px; letter-spacing: 10px; line-height: 48px;
    padding-left: 10px;
  }
  .headline-main {
    font-family: "Barlow Condensed", "Arial Narrow", sans-serif;
    font-weight: 700; font-size: 90px; line-height: 76px; color: var(--yellow);
    letter-spacing: 8px; padding-left: 8px;
  }
  .question {
    position: absolute; left: 0; top: 458px; width: 848px; text-align: center;
    font-weight: 600; font-size: 30px;
  }
  .parts-band {
    position: absolute; left: 0; top: 548px; width: 848px; height: 216px; background: var(--white);
  }
  .part-photo {
    position: absolute; border-radius: 18px;
    background: linear-gradient(160deg, var(--photo-steel), var(--photo-dark));
  }
  .benefits {
    position: absolute; left: 0; top: 805px; width: 848px;
    display: flex; justify-content: center; gap: 26px;
  }
  .benefit { width: 103px; text-align: center; }
  .benefit-icon {
    width: 103px; height: 103px; border-radius: 50%; background: var(--yellow);
    display: flex; align-items: center; justify-content: center;
  }
  .benefit-label { margin-top: 14px; font-size: 14px; line-height: 17px; color: var(--label); white-space: nowrap; margin-left: -20px; margin-right: -20px; }
  .aim-band {
    position: absolute; left: 0; top: 977px; width: 848px; height: 60px; background: var(--yellow);
  }
  .aim-tab {
    position: absolute; left: 275px; top: 1030px; width: 298px; height: 40px;
    background: var(--yellow); border-radius: 0 0 30px 30px;
  }
  .aim-text {
    position: absolute; left: 0; top: 989px; width: 848px; text-align: center;
    font-family: "Barlow Condensed", "Arial Narrow", sans-serif;
    font-weight: 600; font-size: 26px; line-height: 33px; color: var(--ink);
  }
  .aim-text strong { font-weight: 700; }
  .footer { position: absolute; left: 0; top: 1070px; width: 848px; height: 130px; background: var(--footer); }
  .footer-band { position: absolute; left: 0; top: 1037px; width: 848px; height: 33px; background: var(--footer); }
  .address { position: absolute; left: 38px; top: 1088px; display: flex; gap: 8px; font-size: 16px; line-height: 23px; font-style: normal; }
  .tollfree { position: absolute; left: 274px; top: 1081px; width: 300px; text-align: center; }
  .tollfree-icon { width: 44px; height: 44px; border-radius: 50%; background: var(--yellow); margin: 0 auto; display: flex; align-items: center; justify-content: center; }
  .tollfree-label { margin-top: 10px; font-weight: 500; font-size: 16px; letter-spacing: 0.5px; }
  .tollfree-number { font-weight: 700; font-size: 37px; line-height: 40px; color: var(--yellow); }
  .contact { position: absolute; left: 558px; top: 1079px; list-style: none; font-size: 15px; line-height: 22px; }
  .contact li { display: flex; align-items: center; gap: 6px; }
  .contact .link { color: var(--yellow); }
</style>
</head>
<body>
<main class="flyer">
  <div class="coil-photo" role="img" aria-label="Coiled steel brake cable"></div>
  <svg class="swoosh" width="848" height="1200" viewBox="0 0 848 1200" aria-hidden="true">
    <path d="M0 0 H420 C540 30 620 80 650 112 C420 150 170 260 0 498 Z" fill="var(--yellow)"/>
  </svg>

  <div class="brand"><span class="brand-square"></span>Summit Brake Works</div>
  <div class="lever-photo" role="img" aria-label="Handbrake lever bracket"></div>
  <div class="caliper-photo" role="img" aria-label="Reconditioned brake caliper"></div>
  <p class="tagline">The Brake and<br>Cable Specialists</p>

  <h1 class="headline">
    <span class="headline-top">STAINLESS STEEL</span><br>
    <span class="headline-main">RESLEEVING</span>
  </h1>
  <h2 class="question">Why re-sleeve your cylinders?</h2>

  <section class="parts-band">
    <div class="part-photo" style="left:105px;top:-14px;width:168px;height:120px" role="img" aria-label="Brake booster housing"></div>
    <div class="part-photo" style="left:327px;top:-20px;width:159px;height:183px" role="img" aria-label="Clutch slave cylinder"></div>
    <div class="part-photo" style="left:519px;top:-29px;width:228px;height:135px" role="img" aria-label="Hydraulic brake booster"></div>
    <div class="part-photo" style="left:198px;top:115px;width:186px;height:120px" role="img" aria-label="Brake master cylinder with reservoir"></div>
    <div class="part-photo" style="left:498px;top:118px;width:201px;height:114px" role="img" aria-label="Wheel cylinder"></div>
  </section>

  <section class="benefits">
    <div class="benefit">
      <div class="benefit-icon">
        <svg width="60" height="60" viewBox="0 0 60 60" fill="none" stroke="var(--ink)" stroke-width="3.5"><circle cx="30" cy="30" r="20"/><text x="30" y="39" text-anchor="middle" font-family="Barlow, sans-serif" font-size="26" font-weight="700" fill="var(--ink)" stroke="none">$</text></svg>
      </div>
      <p class="benefit-label">Cost<br>effective</p>
    </div>
    <div class="benefit">
      <div class="benefit-icon">
        <svg width="64" height="64" viewBox="0 0 64 64" fill="none" stroke="var(--ink)" stroke-width="6"><path d="M12 32 A20 20 0 1 1 20 48"/><path d="M32 20 V33 L41 40" stroke-linecap="round"/><path d="M4 28 L12 38 L20 28 Z" fill="var(--ink)" stroke="none"/></svg>
      </div>
      <p class="benefit-label">Long<br>Lasting</p>
    </div>
    <div class="benefit">
      <div class="benefit-icon">
        <svg width="76" height="40" viewBox="0 0 76 40" fill="var(--ink)"><rect x="12" y="6" width="4" height="14"/><rect x="18" y="12" width="6" height="8"/><rect x="28" y="8" width="10" height="5"/><rect x="41" y="8" width="10" height="5"/><rect x="54" y="8" width="10" height="5"/><rect x="28" y="15" width="10" height="5"/><rect x="41" y="15" width="10" height="5"/><rect x="54" y="15" width="10" height="5"/><path d="M2 22 H74 L66 36 H8 Z"/></svg>
      </div>
      <p class="benefit-label">No waiting for<br>overseas parts</p>
    </div>
    <div class="benefit">
      <div class="benefit-icon">
        <svg width="60" height="60" viewBox="0 0 60 60" fill="none" stroke="var(--ink)" stroke-width="6" stroke-linejoin="round"><path d="M22 18 L30 6 L38 18"/><path d="M44 26 L52 40 H40"/><path d="M20 46 H8 L14 34"/><path d="M30 6 L44 28"/><path d="M52 40 H22"/><path d="M8 46 L22 22"/></svg>
      </div>
      <p class="benefit-label">Re-manufacturing<br>= Re-cycling</p>
    </div>
    <div class="benefit">
      <div class="benefit-icon">
        <svg width="64" height="64" viewBox="0 0 64 64" fill="none" stroke="var(--ink)" stroke-width="4"><rect x="22" y="6" width="20" height="10"/><circle cx="32" cy="38" r="20"/><path d="M10 14 L54 58 M54 14 L10 58"/></svg>
      </div>
      <p class="benefit-label">Cylinders are no<br>longer available</p>
    </div>
  </section>

  <div class="aim-band"></div>
  <div class="footer-band"></div>
  <div class="aim-tab"></div>
  <p class="aim-text">Our aim is to have your parts repaired within the quickest<br><strong>Turn-around Time</strong> possible!</p>

  <footer class="footer"></footer>
  <address class="address">
    <svg width="18" height="24" viewBox="0 0 18 24"><path d="M9 0 C4 0 0 4 0 9 C0 15 9 24 9 24 C9 24 18 15 18 9 C18 4 14 0 9 0 Z" fill="var(--yellow)"/><circle cx="9" cy="9" r="3.5" fill="var(--footer)"/></svg>
    <span>Summit Brake Works<br>24 Harwood Street<br>Riverton</span>
  </address>

  <div class="tollfree">
    <div class="tollfree-icon">
      <svg width="24" height="24" viewBox="0 0 24 24"><path d="M6 2 L9 7 L7 9.5 C8.5 12.5 11.5 15.5 14.5 17 L17 15 L22 18 L20 22 C11 22 2 13 2 4 Z" fill="var(--footer)"/></svg>
    </div>
    <p class="tollfree-label">TOLL FREE NUMBER</p>
    <p class="tollfree-number">0800 55 01 44</p>
  </div>

  <ul class="contact">
    <li><svg width="14" height="14" viewBox="0 0 24 24"><path d="M6 2 L9 7 L7 9.5 C8.5 12.5 11.5 15.5 14.5 17 L17 15 L22 18 L20 22 C11 22 2 13 2 4 Z" fill="var(--yellow)"/></svg>Phone: 07 555 0142</li>
    <li><svg width="14" height="14" viewBox="0 0 14 14" fill="none" stroke="var(--yellow)" stroke-width="1.4"><rect x="1" y="5" width="12" height="8"/><rect x="4" y="1" width="6" height="4"/></svg>Fax: 07 555 0143</li>
    <li><svg width="14" height="14" viewBox="0 0 14 14" fill="none" stroke="var(--yellow)" stroke-width="1.4"><rect x="1" y="3" width="12" height="8"/><path d="M1 3 L7 8 L13 3"/></svg><span>Email: <span class="link">parts@summitbrakeworks.co.nz</span></span></li>
    <li><svg width="14" height="14" viewBox="0 0 14 14" fill="none" stroke="var(--yellow)" stroke-width="1.2"><circle cx="7" cy="7" r="6"/><ellipse cx="7" cy="7" rx="2.5" ry="6"/><path d="M1 7 H13"/></svg><span class="link">www.summitbrakeworks.co.nz</span></li>
  </ul>
</main>
</body>
</html>
```